Dynamic Templates

Our company hosts web stores for our clients. They can set up as many as they wish on our platform, and select from the stock templates we provide. We are looking to increase the number of available stock templates.

Because our users can dynamically control many of the template elements - specifically colors - they have to be flexible and abide by certain rules. These rules are spelled out in the attached documents.

Here are links to two of our most used templates:
http://fernridge.vexalcart.example/
http://stampled.vexalcart.example/

Templates need to have a landing page (what you see when first clicking one of the above links). There also needs to be a category page (what you see when clicking any category) and a product detail page (what you see when you arrive at an individual product, where there are various cart options like Buy Now or Request Info).

```html
<!DOCTYPE html>
<html lang="en">
<head>
<meta charset="utf-8">
<title>BrightCrate – Promotional Products</title>
<link href="https://fonts.googleapis.com/css2?family=PT+Sans:wght@400;700&family=Noto+Sans:wght@400;700&display=swap" rel="stylesheet">
<style>
  :root{
    --orange:#f7941d;
    --orange-text:#f37a12;
    --navy:#05345a;
    --page-grey:#e8e8e8;
    --ink:#000;
    --body-ink:#333;
    --footer:#333;
    --white:#fff;
  }
  *{box-sizing:border-box;margin:0;padding:0}
  html,body{width:982px;height:1200px;overflow:hidden;background:var(--page-grey)}
  body{font-family:"Noto Sans",sans-serif;color:var(--ink)}
  .page{position:relative;width:1002px;height:1224px;transform:scale(0.98);transform-origin:0 0;
        background:linear-gradient(var(--white) 0 224px,var(--page-grey) 224px)}
  .brand{position:absolute;left:62px;top:52px;display:flex;align-items:center;gap:10px}
  .brand-dot{width:42px;height:42px;border-radius:50%;background:var(--orange)}
  .brand-name{font-family:"PT Sans",sans-serif;font-weight:700;font-size:22px;color:var(--navy)}
  .contact-line{position:absolute;right:58px;top:61px;font-size:11.5px;font-weight:700}
  .contact-line a{color:var(--orange-text);text-decoration:none}
  .banner{position:absolute;left:50px;top:127px;width:902px;height:194px;border:3px solid var(--orange);
          border-radius:30px;background:var(--white);display:flex;justify-content:space-around;align-items:center;padding:0 20px}
  .banner .product{height:170px;border-radius:8px}
  .sidebar{position:absolute;left:50px;top:334px;width:207px}
  .side-title{font-family:"PT Sans",sans-serif;font-size:18px;text-align:center;margin-left:-10px}
  .search{margin-top:10px;height:30px;border:3px solid var(--orange);border-radius:15px;background:var(--white);position:relative}
  .search-go{position:absolute;right:1px;top:1px;width:40px;height:22px;border-radius:11px;background:var(--navy);
             color:var(--white);font-family:"PT Sans",sans-serif;font-size:17px;line-height:22px;text-align:center}
  .panel{background:var(--orange);border-radius:22px;padding:9px 11px 26px}
  .panel+.panel,.search+.panel{margin-top:11px}
  .panel-head{height:48px;border:3px solid var(--white);border-radius:24px;background:var(--navy);color:var(--white);
              font-family:"PT Sans",sans-serif;font-size:18px;line-height:42px;text-align:center}
  .panel ul{list-style:none;margin:17px 0 0 7px}
  .panel li{height:25px;border-bottom:1px solid #fbc27e;font-size:11px;font-weight:700;line-height:22px;padding-left:17px;position:relative}
  .panel li::before{content:"";position:absolute;left:3px;top:8px;border:4px solid transparent;border-left:5px solid var(--white)}
  .content{position:absolute;left:275px;top:366px;width:676px}
  .content h2{font-family:"PT Sans",sans-serif;font-weight:400;font-size:18px;color:var(--orange-text);
              padding-bottom:5px;border-bottom:1px dashed #777;margin-bottom:9px}
  .content p{font-size:10.5px;line-height:18px;margin-bottom:18px}
  .content p.muted{color:var(--body-ink)}
  .content h2.second{margin-top:24px}
  .bag{position:absolute;left:790px;top:603px;width:162px;height:207px;border-radius:4px;
       background:linear-gradient(135deg,#e0242b 0%,#b3121a 70%,#555 100%)}
  .shop-cta{position:absolute;left:790px;top:822px;width:155px;text-align:center;font-family:"PT Sans",sans-serif;font-size:18px}
  .contact-box{position:absolute;left:794px;top:871px;width:158px;height:96px;border:3px solid var(--orange);border-radius:20px;
               background:var(--white);text-align:center;padding-top:9px}
  .contact-box h3{font-family:"PT Sans",sans-serif;font-weight:400;font-size:18px;margin-bottom:4px}
  .contact-box a{display:block;font-size:11px;font-weight:700;color:var(--orange-text);text-decoration:none;line-height:16px}
  .footer{position:absolute;left:0;top:1173px;width:1002px;height:51px;background:var(--footer);color:var(--white);
          font-size:10px;text-align:center;line-height:52px}
</style>
</head>
<body>
<div class="page">
  <header>
    <div class="brand"><span class="brand-dot"></span><span class="brand-name">BrightCrate</span></div>
    <div class="contact-line">Demo User . (555) 014-2290 . <a href="#">info@brightcrate.example</a></div>
    <div class="banner">
      <div class="product" role="img" aria-label="Colourful puzzle desk ornament" style="width:170px;background:linear-gradient(#7fc6e8,#2b2b2b)"></div>
      <div class="product" role="img" aria-label="Branded desk calculator" style="width:135px;background:linear-gradient(#d9dde2,#2a56b0)"></div>
      <div class="product" role="img" aria-label="Squeeze hammer toy" style="width:70px;background:linear-gradient(#f1e85a,#5aa9e6)"></div>
      <div class="product" role="img" aria-label="Leather portfolio with pen and USB drive" style="width:160px;background:linear-gradient(#3a3a3a,#111)"></div>
    </div>
  </header>

  <aside class="sidebar">
    <div class="side-title">Quick Search</div>
    <div class="search"><span class="search-go">Go</span></div>
    <nav class="panel">
      <div class="panel-head">Shop By Category</div>
      <ul>
        <li>Apparel</li><li>Auto</li><li>Bags &amp; Totes Caps &amp;</li><li>Hats Computer Eco</li>
        <li>Friendly Food, Candy &amp;</li><li>Drink Golf, Sports &amp;</li><li>Outdoors Home &amp;</li>
        <li>House wares</li><li>Notebooks &amp; Folios</li><li>Tools &amp; Hardware</li><li>Writing Instruments</li>
        <li>Business Supplies</li><li>Clocks &amp; Watches</li><li>Corporate Gifts</li><li>Electronics Games</li>
      </ul>
    </nav>
    <nav class="panel">
      <div class="panel-head">Shop By Price</div>
      <ul>
        <li>Under $5</li><li>$5 - $10</li><li>$10 - $20</li><li>$20 - $50</li>
        <li>$50 - $100</li><li>$100 - $200</li><li>Over $200</li>
      </ul>
    </nav>
  </aside>

  <main class="content">
    <h2>Welcome To The Future of Promotional Products!</h2>
    <p>Gone are the days of searching through dog-eared catalogs or trying to make sense of complicated product websites.</p>
    <p>We do the work for you! We've taken only the very best and most current products and placed them in easy-to-use categories designed for your needs. Take a look at our selection - quality products at excellent prices.</p>
    <h2 class="second">Enjoy This Amazing New Resource</h2>
    <p class="muted">We know you don't have time to waste; so we've cut to the chase and made it simple! But keep in mind, we do have access to over a million products - so if you don't see what you're looking for or have a special theme or request, let us know - we'll find it!</p>
  </main>

  <div class="bag" role="img" aria-label="Red gift shopping bag with snowflake pattern"></div>
  <div class="shop-cta">Start Shopping</div>
  <div class="contact-box">
    <h3>Contact Us</h3>
    <a href="#">info@brightcrate.example</a>
    <a href="#">www.brightcrate.example</a>
  </div>

  <footer class="footer">Copyright © 2010 . BrightCrate.example V3 . All Rights Reserved.</footer>
</div>
</body>
</html>
```